Double sided 8.5x11 Flyer

The attached text should be in the flyer. this is an election flyer for a board of director role for automotive racing industry. Try to make it exciting!

```html
<!DOCTYPE html>
<html lang="en">
<head>
<meta charset="utf-8">
<title>Daniel Carver for AMPA Director – Flyer</title>
<link href="https://fonts.googleapis.com/css2?family=Bebas+Neue&family=Arimo:wght@400;700&display=swap" rel="stylesheet">
<style>
:root{
  --navy:#0d1a5c;
  --red:#e0161b;
  --ink:#333333;
  --headline-gray:#3a3a3a;
  --row-gray:#efeff1;
  --row-gray-alt:#e6e6ea;
  --line-gray:#d6d6da;
  --footer:#232323;
  --link:#3d8bff;
  --canvas:#e8e8e8;
}
*{box-sizing:border-box;margin:0;padding:0}
html,body{width:800px;height:1200px;overflow:hidden;background:var(--canvas)}
body{position:relative;font-family:"Arimo",Arial,sans-serif;color:var(--ink)}
.sheet-slot{position:absolute;left:172px;width:456px;height:590px;box-shadow:0 3px 10px rgba(0,0,0,.22);overflow:hidden}
.sheet-slot.front{top:6px}
.sheet-slot.back{top:604px}
.sheet{position:absolute;left:0;top:0;width:680px;height:880px;background:#fff;overflow:hidden;transform:scale(.6706);transform-origin:0 0}
.flag-backdrop{position:absolute;left:0;top:0}

/* front */
.candidate-photo{position:absolute;left:432px;top:22px;width:200px;height:340px;border-radius:90px 90px 6px 6px;background:linear-gradient(180deg,#c9a58c 0%,#b48b72 22%,#1c2233 36%,#141a2a 100%)}
.headline{position:absolute;left:46px;top:52px;font-family:"Bebas Neue",Impact,sans-serif;font-weight:400;color:var(--headline-gray);font-size:57px;line-height:.93;letter-spacing:.5px}
.headline .accent{display:block;color:var(--navy);font-size:142px;line-height:.86;letter-spacing:1px}
.intro{position:absolute;left:45px;top:432px;width:262px;color:#fff;font-size:9.6px;line-height:1.27;text-align:justify}
.intro p{margin-bottom:19px}
.platform{position:absolute;left:362px;top:462px;width:288px}
.platform-item{position:relative;padding-left:38px;font-size:9.6px;line-height:1.27;text-align:justify;margin-bottom:15px}
.platform-item.first{padding-right:40px;text-align:left}
.platform-item strong{font-weight:700}
.platform-icon{position:absolute;left:0;top:-2px;width:28px;height:28px}
.timeline{position:absolute;left:376px;top:488px;width:1px;height:322px;border-left:1.4px dashed var(--red)}
.timeline-end{position:absolute;left:373px;top:808px;width:7px;height:7px;border-radius:50%;background:var(--red)}
.passion-list{list-style:none;margin-top:7px}
.passion-list li{position:relative;padding-left:14px;margin-bottom:5px;text-align:left}
.passion-list svg{position:absolute;left:0;top:1px;width:9px;height:9px}

/* shared footer */
.sheet-footer{position:absolute;left:0;bottom:0;width:680px;height:57px;background:var(--footer);color:#fff;font-size:8.4px;line-height:1.3;text-align:center;padding:16px 50px 0}
.sheet-footer .link{color:var(--link)}

/* back */
.section-header{position:absolute;left:42px;top:32px;width:598px;height:40px;background:var(--red);border-radius:9px 9px 0 0;color:#fff;font-weight:700;font-size:16.5px;line-height:40px;text-align:center;letter-spacing:.2px}
.achievements{position:absolute;left:42px;top:72px;width:598px;display:grid;grid-template-columns:1fr 1fr;background:#fff}
.achievement{padding:7px 18px 7px;font-size:9.2px;line-height:1.26;height:72px;overflow:hidden}
.achievement:nth-child(4n+3),.achievement:nth-child(4n+4){background:var(--row-gray)}
.achievement:nth-child(odd){border-right:1px solid var(--line-gray)}
.achievement h3{color:var(--navy);font-size:10.8px;font-weight:700;margin-bottom:3px;line-height:1.2}
.workshop-photo{position:absolute;left:42px;top:448px;width:598px;height:158px;background:linear-gradient(100deg,#3a4a66 0%,#7d8da6 35%,#5c6f8d 55%,#9aa8bb 75%,#2e3b55 100%)}
.section-title{position:absolute;left:42px;top:622px;color:var(--navy);font-size:16.5px;font-weight:700;letter-spacing:.2px;line-height:20px}
.endorsements{position:absolute;left:42px;top:648px;width:598px;border-collapse:collapse;font-size:9.2px;line-height:1.2}
.endorsements td,.endorsements th{font-weight:400;text-align:left;vertical-align:top;padding:2px 6px 2px 8px;border-bottom:1px solid #fff}
.endorsements tr{background:var(--row-gray)}
.endorsements tr:nth-child(odd){background:var(--row-gray-alt)}
.endorsements .col-name{width:60px;border-right:1px solid var(--line-gray)}
.endorsements .col-quote{width:170px;border-right:1px solid var(--line-gray)}
.endorsements .col-gap{width:110px;border-right:1px solid var(--line-gray)}
</style>
</head>
<body>

<!-- FRONT SIDE -->
<div class="sheet-slot front">
  <article class="sheet">
    <svg class="flag-backdrop" width="680" height="880" viewBox="0 0 680 880">
      <defs>
        <linearGradient id="flagWave" x1="0" y1="0" x2="1" y2="0.6">
          <stop offset="0" stop-color="#ffffff"/>
          <stop offset="0.35" stop-color="#f6dede"/>
          <stop offset="0.55" stop-color="#e9a7a8"/>
          <stop offset="0.8" stop-color="#ffffff"/>
          <stop offset="1" stop-color="#f3d3d4"/>
        </linearGradient>
        <linearGradient id="starField" x1="0" y1="0" x2="1" y2="1">
          <stop offset="0" stop-color="#2a3f8f"/>
          <stop offset="1" stop-color="#14237a"/>
        </linearGradient>
      </defs>
      <g role="img" aria-label="Waving stars and stripes flag backdrop">
        <rect x="0" y="0" width="680" height="440" fill="url(#flagWave)"/>
        <path d="M430 0 H680 V300 C600 260 520 200 470 120 C450 80 440 40 430 0 Z" fill="url(#starField)"/>
      </g>
      <path d="M0 296 C200 400 430 380 680 250 L680 300 C430 420 200 430 0 336 Z" fill="var(--red)"/>
      <path d="M0 330 C200 430 430 410 680 290 L680 880 L0 880 Z" fill="var(--navy)"/>
      <path d="M338 436 C470 412 580 418 680 446 L680 820 L338 820 Z" fill="#fff"/>
      <path d="M338 436 C470 412 580 418 680 446 L680 426 C580 398 470 394 338 420 Z" fill="#1e3fae"/>
    </svg>

    <div class="candidate-photo" role="img" aria-label="Portrait of the candidate in a dark suit and lavender tie, smiling"></div>

    <h1 class="headline">New cars<br>are not designed<br>with modification<span class="accent">In mind</span></h1>

    <section class="intro">
      <p>You are probably aware that some autonomous vehicle technology is showing up as features in cars today and will be mandated in a few years. This Technology is called ADAS, or Advanced Driver Assist Systems. What you may not know is that ADAS systems can malfunction when vehicles are modified. Not just performance and racing, this affects wheels and tires, body modifications, paint (yes, increasing paint thickness on a bumper can cause these systems to read distances wrong), interior changes, and so much more. If we don't get in front of ADAS as an aftermarket industry, vehicle customization will impact driver safety and we can expect government regulation preventing modification and limiting our future of vehicle customization.</p>
      <p>I can't stand to the side and watch this happen. I love performance cars, racing, vehicle modification, and customization. I managed KVT and several other startups, I modify my own cars and my daily driver has 1000 HP, I have a NDRA competition license, and I believe that for many AMPA members the opportunity to customize is a way of life.</p>
      <p>I am running for AMPA director because I can drive change. I have made real change in the repair industry thru right to repair and Automaker relationships, and I have the experience, relationships, leadership, motivation, and drive to push the full force of AMPA towards this problem before it's too late. All I need to get started is your vote.</p>
    </section>

    <div class="timeline"></div>
    <div class="timeline-end"></div>

    <section class="platform">
      <div class="platform-item first">
        <svg class="platform-icon" viewBox="0 0 28 28"><circle cx="14" cy="14" r="13" fill="#fff" stroke="var(--navy)" stroke-width="1.3"/><circle cx="14" cy="14" r="8" fill="none" stroke="var(--navy)" stroke-width="1"/><rect x="13.2" y="9" width="1.6" height="6.5" fill="var(--navy)"/><circle cx="14" cy="18" r="1" fill="var(--navy)"/></svg>
        <strong>Problem:</strong> ADAS systems often stop functioning when a vehicle is modified
      </div>
      <div class="platform-item">
        <svg class="platform-icon" viewBox="0 0 28 28"><circle cx="14" cy="14" r="13" fill="#fff" stroke="var(--navy)" stroke-width="1.3"/><circle cx="14" cy="14" r="4" fill="none" stroke="var(--navy)" stroke-width="1.2"/><path d="M14 6v3M14 19v3M6 14h3M19 14h3M8.5 8.5l2 2M17.5 17.5l2 2M19.5 8.5l-2 2M10.5 17.5l-2 2" stroke="var(--navy)" stroke-width="1.2"/></svg>
        My Solution is to activate the Full strength of AMPA and it's network to engage Automakers, Regulators, and Industry. Vehicles must be designed with modification in mind, and there must be a partnership and transparency with the aftermarket.
      </div>
      <div class="platform-item">
        <svg class="platform-icon" viewBox="0 0 28 28"><circle cx="14" cy="14" r="13" fill="#fff" stroke="var(--navy)" stroke-width="1.3"/><circle cx="14" cy="10" r="2.4" fill="none" stroke="var(--navy)" stroke-width="1.1"/><circle cx="9" cy="13" r="2" fill="none" stroke="var(--navy)" stroke-width="1.1"/><circle cx="19" cy="13" r="2" fill="none" stroke="var(--navy)" stroke-width="1.1"/><path d="M9 20c0-3 2-5 5-5s5 2 5 5" fill="none" stroke="var(--navy)" stroke-width="1.1"/></svg>
        I bring my Leadership and Experience as President of Vantor IVS, a technology business that helps technicians with complex vehicles repairs and ADAS calibration, previous General Manager of KVT, experience with right to repair regulations, Automaker and government relationships, Inventor on over 60 patents.
      </div>
      <div class="platform-item">
        <svg class="platform-icon" viewBox="0 0 28 28"><circle cx="14" cy="14" r="13" fill="#fff" stroke="var(--navy)" stroke-width="1.3"/><path d="M14 7a5 5 0 0 0-3 9v2h6v-2a5 5 0 0 0-3-9z" fill="none" stroke="var(--navy)" stroke-width="1.1"/><path d="M11.5 20h5M12.5 22h3" stroke="var(--navy)" stroke-width="1.1"/></svg>
        <strong>My Passions keep me motivated</strong>
        <ul class="passion-list">
          <li><svg viewBox="0 0 9 9"><rect x=".5" y=".5" width="8" height="8" fill="none" stroke="var(--red)"/><path d="M2 4.5l2 2 3.5-4.5" fill="none" stroke="var(--red)" stroke-width="1.2"/></svg>Resto-mod projects at home (last was a 75 T4 Roamer powertrain swap)</li>
          <li><svg viewBox="0 0 9 9"><rect x=".5" y=".5" width="8" height="8" fill="none" stroke="var(--red)"/><path d="M2 4.5l2 2 3.5-4.5" fill="none" stroke="var(--red)" stroke-width="1.2"/></svg>Fast Cars (1000 HP Daily Driver RS-8)</li>
          <li><svg viewBox="0 0 9 9"><rect x=".5" y=".5" width="8" height="8" fill="none" stroke="var(--red)"/><path d="M2 4.5l2 2 3.5-4.5" fill="none" stroke="var(--red)" stroke-width="1.2"/></svg>NDRA Comp Licensed Driver</li>
          <li><svg viewBox="0 0 9 9"><rect x=".5" y=".5" width="8" height="8" fill="none" stroke="var(--red)"/><path d="M2 4.5l2 2 3.5-4.5" fill="none" stroke="var(--red)" stroke-width="1.2"/></svg>Pilot, multi engine, instrument and Jet rated</li>
          <li><svg viewBox="0 0 9 9"><rect x=".5" y=".5" width="8" height="8" fill="none" stroke="var(--red)"/><path d="M2 4.5l2 2 3.5-4.5" fill="none" stroke="var(--red)" stroke-width="1.2"/></svg>Hobbyist collector car broker</li>
          <li><svg viewBox="0 0 9 9"><rect x=".5" y=".5" width="8" height="8" fill="none" stroke="var(--red)"/><path d="M2 4.5l2 2 3.5-4.5" fill="none" stroke="var(--red)" stroke-width="1.2"/></svg>Hobbyist airplane dealer</li>
          <li><svg viewBox="0 0 9 9"><rect x=".5" y=".5" width="8" height="8" fill="none" stroke="var(--red)"/><path d="M2 4.5l2 2 3.5-4.5" fill="none" stroke="var(--red)" stroke-width="1.2"/></svg>Driving change in whatever I do</li>
        </ul>
      </div>
    </section>

    <footer class="sheet-footer">
      More on these at my website: <span class="link">www.CarverAMPA.com</span> to learn more details on the challenge, my vision for solving these problems, and my credentials and experience to make it happen. You can also contact me directly at <span class="link">daniel.carver@vantorivs.com</span> or <span class="link">(555) 014-2290</span>
    </footer>
  </article>
</div>

<!-- BACK SIDE -->
<div class="sheet-slot back">
  <article class="sheet">
    <svg class="flag-backdrop" width="680" height="880" viewBox="0 0 680 880">
      <defs>
        <linearGradient id="flagCorner" x1="0" y1="0" x2="1" y2="0.4">
          <stop offset="0" stop-color="#f5d6d7"/>
          <stop offset="0.4" stop-color="#e38d8f"/>
          <stop offset="0.55" stop-color="#2a3f8f"/>
          <stop offset="1" stop-color="#17267c"/>
        </linearGradient>
      </defs>
      <path role="img" aria-label="Waving stars and stripes flag corner" d="M300 0 H680 V330 C662 250 655 150 640 60 C560 40 420 30 300 0 Z" fill="url(#flagCorner)"/>
    </svg>

    <h2 class="section-header">Change in the industry I've played a key role in</h2>
    <section class="achievements">
      <div class="achievement"><h3>Standardized Vehicle Diagnostics</h3>As a co-founder of Larkfield Technologies, our company helped realize the industry achieve standardized dealer diagnostics</div>
      <div class="achievement"><h3>Access to factory vehicle diagnostics for everyone</h3>I personally played an active role in Right to Repair</div>
      <div class="achievement"><h3>Modernization of Performance Calibration</h3>I became General Manager of KVT, during its startup phase, and helped that company bring flash tuning and DIY vehicle calibration mainstream</div>
      <div class="achievement"><h3>Keeping Overreaching patents from affecting our industry</h3>By litigating against the biggest companies and winning, I helped re-shaping patent law to protect overreach</div>
      <div class="achievement"><h3>Configurable Gauge Displays</h3>I was a co-inventor of the first user configurable LCD Gauge Display, patented and delivered at AMPA 2007 called GaugeLink. This technology has spread throughout the industry.</div>
      <div class="achievement"><h3>Helping Mechanics support multi-brands of vehicles</h3>I led the acquisition of Motiva and Clearline, which day, under the Vantor IVS Umbrella deliver remote diagnostic assistance using dealer trained techs</div>
      <div class="achievement"><h3>Remote Programming</h3>I was co-inventor of remote programming under Vantor IVS (Known as RMP), allowing remote software updates of vehicles.</div>
      <div class="achievement"><h3>Helping Collision repairers keep cars safe</h3>The company I run (Vantor IVS) helps scan vehicles after collisions and complete ADAS Calibrations that ensures vehicles are safe when they return on the road</div>
      <div class="achievement"><h3>Building Business</h3>I've helped build and recover automotive businesses, from startup to now nearly 400 employees across 7 offices and 3 continents that touch over a million vehicles per year</div>
      <div class="achievement"><h3>Porting Superchargers</h3>Thru the first company I founded, Brellis, I brought supercharger porting to the mainstream for the Stallion GT and Thunder.</div>
    </section>

    <div class="workshop-photo" role="img" aria-label="Technicians in masks and a hard hat reviewing a tablet on a factory floor"></div>

    <h2 class="section-title">Endorsements from Industry</h2>
    <table class="endorsements">
      <tr><th class="col-name">Name</th><th class="col-quote">Quote</th><th class="col-gap"></th><th class="col-name">Name</th><th>Quote</th></tr>
      <tr><td class="col-name">Name<br>Title</td><td class="col-quote">One sentence quote here about<br>Daniel Carver</td><td class="col-gap"></td><td class="col-name">Name<br>Title</td><td>One sentence quote here about<br>Daniel Carver</td></tr>
      <tr><td class="col-name">Name<br>Title</td><td class="col-quote">One sentence quote here about<br>Daniel Carver</td><td class="col-gap"></td><td class="col-name">Name<br>Title</td><td>One sentence quote here about<br>Daniel Carver</td></tr>
      <tr><td class="col-name">Name<br>Title</td><td class="col-quote">One sentence quote here about<br>Daniel Carver</td><td class="col-gap"></td><td class="col-name">Name<br>Title</td><td>One sentence quote here about<br>Daniel Carver</td></tr>
      <tr><td class="col-name">Name<br>Title</td><td class="col-quote">One sentence quote here about<br>Daniel Carver</td><td class="col-gap"></td><td class="col-name">Name<br>Title</td><td>One sentence quote here about<br>Daniel Carver</td></tr>
      <tr><td class="col-name">Name<br>Title</td><td class="col-quote">One sentence quote here about<br>Daniel Carver</td><td class="col-gap"></td><td class="col-name">Name<br>Title</td><td>One sentence quote here about<br>Daniel Carver</td></tr>
    </table>

    <footer class="sheet-footer">
      More on these at my website: <span class="link">www.CarverAMPA.com</span> to learn more details on the challenge, my vision for solving these problems, and my credentials and experience to make it happen. You can also contact me directly at <span class="link">daniel.carver@vantorivs.com</span> or <span class="link">(555) 014-2290</span>
    </footer>
  </article>
</div>

</body>
</html>
```